Business Card Design

We need a new business card design for a CPA office that has been in business for over 10 years. We are a Accounting Concierge firm that offers the following services: Certified Public Accountant, Personal & Business Tax Preparation, Accounting, Bookkeeping, Payroll Services, Tax Litigation Services.
Certified LedgerNest TallyPartner.  We would like to see designs that use the color navy blue in the company logo with classic accent colors.  We would like the card to be on a textured high pound card stock and that is more classic and less modern in design.  The final design should communicate class and professionalism.

Updates
Reason: I gave feedback to many of the designers with some changes.  Please re-read the brief as we would like to remove the photo of the man on the card.  We also want only light grey or white background, not navy or blue - the navy or blue tones should be the font or accent colors.  Please also, consider creating a logo with the initials P&A or PA or P&A CPA.

Industry/Entity Type
Business
Contact Information for Business Card
Pelwick & Associates CPA, Gerald Pelwick III, 5136 Orvale Road West, Suite D, Bradenton, FL  34917, Phone: (555) 318-2276, Fax: (555) 462-7093, Email: Gerald@GPelwickCPA.example, Website: www.GPelwickCPA.example
Requirements
Must have
- LedgerNest Logo

Should not have
- we no longer want the photo on the card.

```html
<!DOCTYPE html>
<html lang="en">
<head>
<meta charset="utf-8">
<title>Pelwick &amp; Associates CPA — Business Card</title>
<link rel="stylesheet" href="https://fonts.googleapis.com/css2?family=Cabin:wght@400;500;600&display=swap">
<style>
  :root {
    --stage: #e9e9ec;
    --card: #ffffff;
    --navy: #27296b;
    --sky: #2a8fd0;
    --ink: #2b2b2f;
    --rule: #5d5f8c;
    --badge: #f6cf1d;
  }
  * { margin: 0; padding: 0; box-sizing: border-box; }
  html, body { width: 1200px; height: 800px; overflow: hidden; background: var(--stage); }
  body { font-family: "Cabin", sans-serif; }

  .card {
    position: absolute; left: 75px; top: 100px;
    width: 1050px; height: 600px;
    background: var(--card);
    box-shadow: 0 6px 24px rgba(0,0,0,.12);
  }
  .contact-top {
    position: absolute; right: 60px; top: 60px;
    text-align: right; font-size: 23px; line-height: 1.45; color: var(--ink);
  }
  .contact-top .email { color: var(--sky); }
  .contact-top .label { color: var(--ink); }

  .firm-name {
    position: absolute; left: 170px; top: 150px;
    font-size: 44px; font-weight: 500; color: var(--navy);
    letter-spacing: .5px; white-space: nowrap;
  }
  .tagline {
    position: absolute; left: 236px; top: 207px;
    font-size: 28px; color: var(--sky); white-space: nowrap;
  }
  .divider {
    position: absolute; left: 150px; top: 256px;
    width: 640px; border-top: 2px dotted var(--rule);
  }
  .services {
    position: absolute; font-size: 22px; color: var(--navy); white-space: nowrap;
  }
  .services .sep { color: var(--sky); margin: 0 10px; }
  .services-1 { left: 150px; top: 275px; }
  .services-2 { left: 88px; top: 310px; }

  .address {
    position: absolute; left: 70px; top: 370px;
    font-size: 22px; line-height: 1.42; color: var(--ink);
  }
  .address .web { color: var(--sky); }

  .partner-badge {
    position: absolute; right: 70px; bottom: 50px;
    width: 115px; height: 115px;
  }
</style>
</head>
<body>
  <div class="card">
    <div class="contact-top">
      <div><span class="label">M:</span> (555) 318-2276 &nbsp;<span class="label">F:</span> (555) 462-7093</div>
      <div><span class="label">E:</span> <span class="email">Gerald@GPelwickCPA.example</span></div>
    </div>

    <h1 class="firm-name">PELWICK &amp; ASSOCIATES CPA, LLC</h1>
    <p class="tagline">Full Service Tax and Accounting</p>
    <div class="divider"></div>

    <p class="services services-1">Certified Public Accountant<span class="sep">/</span>Personal &amp; Business Tax Preparation</p>
    <p class="services services-2">Bookkeeping<span class="sep">/</span>Accounting<span class="sep">/</span>Payroll Services<span class="sep">/</span>Tax Litigation Services</p>

    <address class="address" style="font-style:normal">
      <div>A: Pelwick &amp; Associates CPA, Gerald Pelwick</div>
      <div>5136 Orvale Road West, Suite D, Bradenton,</div>
      <div>FL 34917.</div>
      <div>W: <span class="web">www.GPelwickCPA.example</span></div>
    </address>

    <svg class="partner-badge" viewBox="0 0 100 100" role="img" aria-label="Certified LedgerNest TallyPartner badge">
      <circle cx="50" cy="50" r="48" fill="var(--badge)"/>
    </svg>
  </div>
</body>
</html>
```